Family owned plumbing contractor needs eye catching business card design

Business cards that are unique, eye catching, and provide customers with general company information, such as name, address, phone number, website, employee name/title, cell phone #, & email address. We are transitioning to a new logo that utilizes a more retro feel, so we are interested in seeing some cool old school designs in the mix. We are liking the dark background on some of the samples on this website. If that is workable with our artwork, we would like to see that incorporated into the design.
Contact Information for Business Card
Copperline Pipeworks, Inc.
www.copperlinepipeworks.example
(555) 392-7068 phone
Nevada License #64205
California License #5810473
Dale Wrennick, President
(555) 618-9032 cell
dale@copperlinepipeworks.example
Residential * Commercial * Service
Requirements
Must have
- The business card details listed above & logo provided.
Nice to have
- I made some notes about color options in the description.

```html
<!DOCTYPE html>
<html lang="en">
<head>
<meta charset="utf-8">
<title>Copperline Pipeworks, Inc. — Business Card</title>
<link href="https://fonts.googleapis.com/css2?family=Lato:wght@400;700&display=swap" rel="stylesheet">
<style>
  :root {
    --backdrop: #161616;
    --card: #252525;
    --card-edge: #2e2e2e;
    --text: #ececec;
    --accent-blue: #5f7e9c;
    --accent-teal: #72c3b4;
  }
  * { box-sizing: border-box; margin: 0; padding: 0; }
  html, body {
    width: 1200px; height: 900px; overflow: hidden;
    background: var(--backdrop);
    font-family: "Lato", sans-serif;
    color: var(--text);
  }
  .sheet {
    position: relative; width: 1200px; height: 900px;
    display: flex; flex-direction: column; align-items: center; justify-content: center; gap: 40px;
  }
  .card {
    position: relative; width: 700px; height: 400px;
    background: var(--card);
    border: 1px solid var(--card-edge);
  }
  .brand {
    display: flex; align-items: center; gap: 14px;
    font-weight: 700; color: var(--accent-teal);
  }
  .brand-dot {
    width: 22px; height: 22px; border-radius: 50%;
    background: var(--accent-teal); flex: none;
  }
  .card-front .brand {
    position: absolute; left: 0; right: 0; top: 165px;
    justify-content: center; font-size: 30px;
  }
  .tagline {
    position: absolute; left: 0; right: 0; bottom: 36px;
    text-align: center; font-size: 18px; letter-spacing: 0.5px;
  }
  .card-back .brand {
    position: absolute; left: 36px; top: 170px; width: 270px;
    font-size: 24px; line-height: 1.2;
  }
  .divider {
    position: absolute; left: 325px; top: 60px; width: 2px; height: 280px;
    background: var(--accent-blue);
  }
  .details { position: absolute; left: 352px; top: 62px; right: 20px; }
  .person-name {
    font-size: 36px; font-weight: 700; color: var(--accent-blue);
    letter-spacing: 1px; text-transform: uppercase; line-height: 1;
  }
  .person-title { font-size: 20px; margin-top: 4px; }
  .licenses { margin-top: 20px; font-size: 19px; line-height: 1.35; }
  .contact-list { list-style: none; margin-top: 16px; font-size: 18px; line-height: 1.55; }
  .contact-list li { display: flex; align-items: center; gap: 10px; white-space: nowrap; }
  .contact-list svg { width: 14px; height: 14px; flex: none; stroke: var(--accent-blue); fill: none; stroke-width: 1.6; }
</style>
</head>
<body>
<main class="sheet">
  <section class="card card-front">
    <div class="brand"><span class="brand-dot"></span>Copperline Pipeworks, Inc.</div>
    <p class="tagline">Residential * Commercial * Service</p>
  </section>

  <section class="card card-back">
    <div class="brand"><span class="brand-dot"></span>Copperline Pipeworks, Inc.</div>
    <div class="divider"></div>
    <div class="details">
      <h1 class="person-name">Dale Wrennick</h1>
      <p class="person-title">President</p>
      <p class="licenses">Nevada License #64205<br>California License #5810473</p>
      <ul class="contact-list">
        <li><svg viewBox="0 0 16 16"><path d="M4 2l2 3-1.5 1.5a8 8 0 0 0 5 5L11 10l3 2-1 2.5C7 14 2 9 1.5 3z"/></svg>(555) 392-7068</li>
        <li><svg viewBox="0 0 16 16"><rect x="4" y="1.5" width="8" height="13" rx="1.5"/><line x1="7" y1="12" x2="9" y2="12"/></svg>(555) 618-9032</li>
        <li><svg viewBox="0 0 16 16"><rect x="1.5" y="3.5" width="13" height="9"/><path d="M1.5 3.5L8 9l6.5-5.5"/></svg>dale@copperlinepipeworks.example</li>
        <li><svg viewBox="0 0 16 16"><circle cx="8" cy="8" r="6.5"/><ellipse cx="8" cy="8" rx="3" ry="6.5"/><line x1="1.5" y1="8" x2="14.5" y2="8"/></svg>www.copperlinepipeworks.example</li>
      </ul>
    </div>
  </section>
</main>
</body>
</html>
```